Coin collector banner ad for specialty insurance

We need a logo designed banner ad (multiple ads) to align with the coin collector market while incorporating color palette logo and call to action. Color palette of Fernholt. Dimension, images, example designs and color palette attached. The context should include 'Specialty Insurance for your coin collection' please refer to the designed examples

Target Market(s)

Coin collectors 30-65+ years of age primarily male

Industry/Entity Type

Insurance

Font styles to use
Sans Serif

Requirements
Must have
• color palette, logo, word mark, Call to Action, The words 'Specialty Insurance for your coin collection'
Nice to have
• Call to actions
Should not have
• ba

```html
<!DOCTYPE html>
<html lang="en">
<head>
<meta charset="UTF-8">
<title>Fernholt Insurance – Specialty Insurance for Your Coin Collection</title>
<link rel="stylesheet" href="https://fonts.googleapis.com/css2?family=Oswald:wght@500;600&family=Jost:wght@400;500&display=swap">
<style>
  :root {
    --white: #ffffff;
    --sky: #29a9e1;
    --azure: #1597d8;
    --royal: #0c57a8;
    --navy: #0a3f86;
    --ink: #1d2230;
    --cta: #17a5df;
    --cta-edge: #0f86c4;
  }
  * { margin: 0; padding: 0; box-sizing: border-box; }
  html, body { width: 1200px; height: 628px; overflow: hidden; background: var(--white); }
  .banner { position: relative; width: 1200px; height: 628px; overflow: hidden; background: var(--white); font-family: "Jost", sans-serif; }
  .backdrop { position: absolute; inset: 0; }
  .brand { position: absolute; top: 40px; left: 822px; display: flex; align-items: center; gap: 26px; }
  .brand-name { color: var(--ink); font-family: "Jost", sans-serif; font-weight: 500; line-height: 1; }
  .brand-name .word { display: block; font-size: 31px; letter-spacing: 0.5px; }
  .brand-name .descriptor { display: block; font-size: 15px; letter-spacing: 7px; margin-top: 8px; }
  .brand-square { width: 84px; height: 84px; background: var(--sky); }
  .headline { position: absolute; right: 83px; top: 165px; text-align: right; }
  .headline .title { font-family: "Oswald", sans-serif; font-weight: 600; font-size: 74px; line-height: 78px; letter-spacing: 7px; color: var(--azure); text-transform: uppercase; margin-right: -7px; }
  .headline .title .lower { color: #1488cf; }
  .headline .subtitle { font-family: "Jost", sans-serif; font-weight: 400; font-size: 27px; letter-spacing: 2.6px; color: var(--ink); margin-top: 12px; text-transform: uppercase; margin-right: -2.6px; }
  .cta { position: absolute; left: 735px; top: 450px; width: 410px; height: 72px; background: var(--cta); border-left: 14px solid var(--cta-edge); display: flex; align-items: center; justify-content: space-between; padding: 0 26px 0 30px; color: var(--white); text-decoration: none; }
  .cta .label { font-family: "Jost", sans-serif; font-weight: 500; font-size: 37px; letter-spacing: 3px; }
  .learn-more { position: absolute; left: 73px; top: 568px; color: var(--white); font-family: "Jost", sans-serif; font-weight: 400; font-size: 30px; letter-spacing: 2.5px; text-decoration: none; }
</style>
</head>
<body>
<div class="banner">
  <svg class="backdrop" width="1200" height="628" viewBox="0 0 1200 628">
    <defs>
      <linearGradient id="panelGrad" x1="0" y1="0" x2="1" y2="1">
        <stop offset="0" stop-color="#36b3e8"/>
        <stop offset="1" stop-color="#1779c8"/>
      </linearGradient>
      <radialGradient id="goldCoin" cx="0.4" cy="0.35" r="0.7">
        <stop offset="0" stop-color="#f3d27a"/>
        <stop offset="0.6" stop-color="#c9982e"/>
        <stop offset="1" stop-color="#7d5a14"/>
      </radialGradient>
      <radialGradient id="proofCoin" cx="0.45" cy="0.4" r="0.7">
        <stop offset="0" stop-color="#f2f2f2"/>
        <stop offset="0.55" stop-color="#9a9a9a"/>
        <stop offset="1" stop-color="#1e1e1e"/>
      </radialGradient>
      <radialGradient id="darkCoin" cx="0.5" cy="0.45" r="0.7">
        <stop offset="0" stop-color="#d8d8d8"/>
        <stop offset="0.5" stop-color="#6d6d6d"/>
        <stop offset="1" stop-color="#1a1a1a"/>
      </radialGradient>
      <radialGradient id="silverCoin" cx="0.5" cy="0.45" r="0.7">
        <stop offset="0" stop-color="#e6e4df"/>
        <stop offset="0.7" stop-color="#b7b3aa"/>
        <stop offset="1" stop-color="#8c877c"/>
      </radialGradient>
    </defs>

    <!-- left panel -->
    <polygon points="0,0 250,0 660,628 0,628" fill="url(#panelGrad)"/>
    <polygon points="0,110 0,628 610,628" fill="var(--royal)" opacity="0.85"/>
    <polygon points="0,330 0,628 300,628" fill="var(--navy)" opacity="0.6"/>

    <!-- lower right bands -->
    <polygon points="520,628 1200,405 1200,628" fill="var(--sky)"/>
    <polygon points="760,628 1200,480 1200,628" fill="var(--royal)"/>

    <!-- connectors -->
    <g stroke="var(--navy)" stroke-width="7">
      <line x1="318" y1="310" x2="180" y2="183"/>
      <line x1="318" y1="310" x2="453" y2="183"/>
      <line x1="318" y1="310" x2="180" y2="445"/>
      <line x1="318" y1="310" x2="453" y2="445"/>
    </g>

    <!-- coin frames -->
    <g class="coin-frames">
      <circle cx="180" cy="183" r="127" fill="var(--navy)"/>
      <circle cx="180" cy="183" r="117" fill="var(--white)"/>
      <circle cx="453" cy="183" r="127" fill="var(--navy)"/>
      <circle cx="453" cy="183" r="117" fill="var(--white)"/>
      <circle cx="180" cy="445" r="127" fill="var(--navy)"/>
      <circle cx="180" cy="445" r="117" fill="var(--white)"/>
      <circle cx="453" cy="445" r="127" fill="var(--navy)"/>
      <circle cx="453" cy="445" r="117" fill="var(--white)"/>
    </g>

    <circle cx="180" cy="183" r="112" fill="url(#goldCoin)" role="img" aria-label="Gold bullion coin, obverse portrait"/>
    <circle cx="453" cy="183" r="112" fill="url(#proofCoin)" role="img" aria-label="Silver proof coin, walking figure design"/>
    <circle cx="180" cy="445" r="112" fill="url(#darkCoin)" role="img" aria-label="Toned silver dollar, eagle reverse"/>
    <circle cx="453" cy="445" r="112" fill="url(#silverCoin)" role="img" aria-label="Silver dollar, eagle reverse"/>

    <!-- hub -->
    <circle cx="318" cy="310" r="34" fill="var(--white)" stroke="var(--navy)" stroke-width="7"/>
    <circle cx="318" cy="310" r="21" fill="var(--navy)"/>
  </svg>

  <div class="brand">
    <div class="brand-name">
      <span class="word">FERNHOLT</span>
      <span class="descriptor">INSURANCE</span>
    </div>
    <div class="brand-square"></div>
  </div>

  <div class="headline">
    <h1 class="title">Specialty<br><span class="lower">Insurance</span></h1>
    <p class="subtitle">For your coin collection</p>
  </div>

  <a class="cta" href="#">
    <span class="label">GET STARTED</span>
    <svg width="46" height="46" viewBox="0 0 46 46" aria-hidden="true">
      <circle cx="23" cy="23" r="20" fill="none" stroke="var(--white)" stroke-width="3"/>
      <polygon points="18,13 32,23 18,33" fill="var(--white)"/>
    </svg>
  </a>

  <a class="learn-more" href="#">LEARN MORE &gt;&gt;</a>
</div>
</body>
</html>
```